Banner Ad Design for Velvet Bridal Shop

Are you a Stylish Designer? Can you work with a balanced color wheel? Let your creative juices flow this way!

```html
<!DOCTYPE html>
<html lang="en">
<head>
<meta charset="utf-8">
<title>Velvet Bridal Shop – Banner</title>
<link href="https://fonts.googleapis.com/css2?family=Raleway:wght@300;400;500&family=Great+Vibes&family=Cormorant+Garamond:wght@500&display=swap" rel="stylesheet">
<style>
  :root {
    --pink-deep: #dfa1ba;
    --pink-mid: #eab6ca;
    --pink-light: #f4cfdc;
    --veil: #f8e6ee;
    --magenta: #b5306a;
    --white: #ffffff;
  }
  html, body {
    margin: 0;
    padding: 0;
    overflow: hidden;
  }
  .banner {
    position: relative;
    width: 1200px;
    height: 290px;
    overflow: hidden;
    background: linear-gradient(90deg, var(--pink-deep) 0%, var(--pink-deep) 14%, var(--pink-mid) 45%, var(--pink-light) 100%);
  }
  .hero-photo {
    position: absolute;
    left: 0;
    top: 0;
    width: 1200px;
    height: 290px;
    background:
      radial-gradient(ellipse 170px 230px at 430px 160px, rgba(255,255,255,0.85), rgba(255,255,255,0) 100%),
      linear-gradient(170deg, rgba(248,230,238,0) 10%, rgba(248,230,238,0.75) 35%, rgba(248,230,238,0.45) 70%, rgba(248,230,238,0) 90%);
  }
  .shipping-offer {
    position: absolute;
    left: 32px;
    top: 58px;
    color: var(--white);
    font-family: "Raleway", sans-serif;
    line-height: 1;
  }
  .shipping-offer .price {
    font-weight: 300;
    font-size: 62px;
    letter-spacing: 1px;
    margin-bottom: 16px;
  }
  .shipping-offer .line {
    font-weight: 400;
    font-size: 26px;
    margin-bottom: 10px;
  }
  .shipping-offer .line.small {
    font-size: 20px;
    margin-top: 6px;
  }
  .tagline {
    position: absolute;
    left: 700px;
    top: 90px;
    width: 460px;
    height: 132px;
    transform: rotate(-33deg);
    transform-origin: center;
    font-family: "Great Vibes", cursive;
    color: var(--magenta);
    font-size: 46px;
    line-height: 44px;
    text-align: center;
  }
  .tagline span {
    display: block;
  }
  .catalogue-band {
    position: absolute;
    left: 0;
    top: 0;
  }
  .catalogue-label {
    font-family: "Cormorant Garamond", serif;
    font-weight: 500;
    font-size: 21px;
    letter-spacing: 1.5px;
    fill: var(--white);
  }
</style>
</head>
<body>
<div class="banner">
  <div class="hero-photo" role="img" aria-label="Photo of a smiling bride in a white gown holding a bouquet, her long veil flowing to the right"></div>

  <div class="shipping-offer">
    <div class="price">$ 10</div>
    <div class="line">FLAT RATE</div>
    <div class="line">SHIPPING</div>
    <div class="line small">STORE WIDE</div>
  </div>

  <div class="tagline">
    <span>New designs &amp;</span>
    <span>products</span>
    <span>arriving daily!</span>
  </div>

  <svg class="catalogue-band" width="1200" height="290" viewBox="0 0 1200 290">
    <polygon points="960,290 1200,140 1200,210 1072,290" fill="var(--magenta)"/>
    <text class="catalogue-label" x="1112" y="230" text-anchor="middle" dominant-baseline="central" transform="rotate(-32 1112 230)">VIEW CATALOGUE</text>
  </svg>
</div>
</body>
</html>
```